Postcard Design

We are a home remodeling company we do a complete home remodeling Including bathrooms ,kitchen ,basement ,interior exterior work .
We doing hardwood floors ,painting ,ceramic tile, baseboards ,casings ,Doors ,drywall repairs, plumbing ,electric,etc ,pretty much everything that has to do with interior and exterior remodeling including Room Additions and New Construction.

As far as the colors and design we would like to keep our company colors.
The attachment I sent with the form that I filled in the Tovik man it's Representing us us as a company as what we do .
Those are the colors that we would like to keep on the flyer so people could recognize us.

Target Market(s)

We would like to target people ho are doing remodeling like kitchen and bathrooms ,basement then people who needs repair and service calls throughout their homes.

Industry/Entity Type

Construction

```html
<!DOCTYPE html>
<html lang="en">
<head>
<meta charset="utf-8">
<title>Remodeling Postcard – Front and Back</title>
<link rel="stylesheet" href="https://fonts.googleapis.com/css2?family=Roboto+Condensed:wght@400;700&display=swap">
<style>
  :root {
    --brand-blue: #2256a8;
    --brand-yellow: #fbb72b;
    --ink: #1b1b1b;
    --paper: #ffffff;
    --stage: #5b5b5b;
    --rule: #9a9a9a;
    --stamp-text: #8a8a8a;
  }
  * { box-sizing: border-box; margin: 0; padding: 0; }
  html, body { width: 782px; height: 1200px; overflow: hidden; }
  body {
    position: relative;
    background: var(--stage);
    font-family: "Roboto Condensed", "Arial Narrow", sans-serif;
  }
  .postcard {
    position: absolute;
    left: 48px;
    width: 682px;
    background: var(--paper);
    overflow: hidden;
  }
  .postcard--front { top: 45px; height: 525px; }
  .postcard--back  { top: 628px; height: 527px; }

  .abs { position: absolute; }

  /* ---------- front ---------- */
  .front-panel {
    left: 0; top: 0; width: 298px; height: 525px;
    background: var(--brand-blue);
    border-right: 6px solid var(--brand-yellow);
  }
  .front-headline {
    left: 22px; top: 18px;
    color: var(--brand-yellow);
    font-weight: 700; font-size: 25px; letter-spacing: -0.2px;
  }
  .service-list { list-style: none; }
  .service-list li {
    display: flex; align-items: center; gap: 10px;
    font-weight: 700;
  }
  .front-services { left: 24px; top: 51px; }
  .front-services li {
    color: var(--paper); font-size: 21px; height: 32.6px;
  }
  .tick { width: 17px; height: 17px; flex: none; }
  .tick--small { width: 15px; height: 15px; }
  .photo-grid {
    left: 24px; top: 255px; width: 246px; height: 246px;
    background: var(--paper); padding: 2px;
    display: grid; grid-template-columns: repeat(3, 1fr); gap: 2px;
  }
  .photo-grid .photo { width: 100%; height: 100%; }
  .photo--a { background: linear-gradient(#eef0ee, #b9b3a8); }
  .photo--b { background: linear-gradient(#f2f2f2, #9b8aa8); }
  .photo--c { background: linear-gradient(#2a2a2a, #9b9690); }
  .photo--d { background: linear-gradient(#3b3b3b, #c9c0b1); }
  .photo--e { background: linear-gradient(#f4f4f4, #cfcfcf); }
  .photo--f { background: linear-gradient(#e7e2dc, #b59aa0); }
  .photo--g { background: linear-gradient(#c7bfb2, #f5f1ea); }
  .photo--h { background: linear-gradient(#f6f6f6, #dcd8d0); }
  .photo--i { background: linear-gradient(#e9e6df, #a88b63); }

  .call-band {
    left: 298px; top: 25px; width: 384px; height: 48px;
    background: var(--brand-yellow);
    color: var(--ink);
    font-weight: 700; font-size: 30px; line-height: 48px;
    padding-left: 14px; letter-spacing: -0.2px;
  }
  .art-house {
    left: 190px; top: 80px; width: 200px; height: 125px;
    border-radius: 6px;
    background: linear-gradient(160deg, #c0282b 0%, #f3e7b6 45%, #fbc531 100%);
  }
  .art-mascot {
    left: 352px; top: 82px; width: 282px; height: 423px;
    border-radius: 10px;
    background: linear-gradient(180deg, #fbc531 0%, #2b5fb0 40%, #2b5fb0 75%, #f2bb2c 100%);
  }

  /* ---------- back ---------- */
  .back-banner-top {
    left: 0; top: 0; width: 510px; height: 157px;
    background: var(--brand-blue);
  }
  .back-banner-side {
    left: 0; top: 157px; width: 329px; height: 85px;
    background: var(--brand-blue);
  }
  .back-mascot {
    left: 22px; top: 24px; width: 170px; height: 206px;
    border-radius: 8px;
    background: linear-gradient(180deg, #fbc531 0%, #2b5fb0 45%, #2b5fb0 75%, #f2bb2c 100%);
  }
  .back-headline {
    left: 196px; top: 18px; width: 276px;
    color: var(--paper); text-align: center;
    font-weight: 700; font-size: 19px; line-height: 25.7px;
  }
  .stamp-box {
    left: 548px; top: 39px; width: 92px; height: 103px;
    border: 1.5px dotted var(--rule);
    color: var(--stamp-text);
    font-size: 16px; line-height: 19px; text-align: center;
    display: flex; align-items: center; justify-content: center;
  }
  .address-area {
    left: 329px; top: 157px; width: 353px; height: 370px;
    background: var(--paper);
    border-left: 1px solid #d4d4d4; border-top: 1px solid #d4d4d4;
  }
  .address-line {
    left: 363px; width: 282px; height: 1px; background: var(--rule);
  }
  .address-line--1 { top: 252px; }
  .address-line--2 { top: 309px; }
  .address-line--3 { top: 367px; }
  .services-panel {
    left: 0; top: 242px; width: 329px; height: 197px;
    background: var(--brand-yellow);
  }
  .services-tab {
    left: 0; top: 12px; width: 202px; height: 27px;
    background: var(--brand-blue);
    clip-path: polygon(0 0, 188px 0, 100% 100%, 0 100%);
    color: var(--brand-yellow);
    font-weight: 700; font-size: 21px; line-height: 27px;
    padding-left: 24px;
  }
  .back-services li {
    color: var(--ink); font-size: 16.5px; height: 28px;
  }
  .back-services--left  { left: 24px;  top: 48px; }
  .back-services--right { left: 206px; top: 48px; }
</style>
</head>
<body>

<svg width="0" height="0" style="position:absolute" aria-hidden="true">
  <defs>
    <symbol id="tick-white" viewBox="0 0 17 17">
      <rect x="1" y="1" width="15" height="15" fill="none" stroke="#ffffff" stroke-width="1.6"/>
      <path d="M4 8.5 L7.3 12 L13 4.5" fill="none" stroke="#ffffff" stroke-width="2"/>
    </symbol>
    <symbol id="tick-ink" viewBox="0 0 17 17">
      <rect x="1" y="1" width="15" height="15" fill="none" stroke="#1b1b1b" stroke-width="1.6"/>
      <path d="M4 8.5 L7.3 12 L13 4.5" fill="none" stroke="#1b1b1b" stroke-width="2"/>
    </symbol>
  </defs>
</svg>

<!-- Front side -->
<section class="postcard postcard--front">
  <div class="abs front-panel"></div>
  <h1 class="abs front-headline">Remodel YOUR</h1>
  <ul class="abs service-list front-services">
    <li><svg class="tick"><use href="#tick-white"/></svg>Home</li>
    <li><svg class="tick"><use href="#tick-white"/></svg>Bathrooms</li>
    <li><svg class="tick"><use href="#tick-white"/></svg>Kitchen</li>
    <li><svg class="tick"><use href="#tick-white"/></svg>Basement</li>
    <li><svg class="tick"><use href="#tick-white"/></svg>Interior</li>
    <li><svg class="tick"><use href="#tick-white"/></svg>Exterior Work.</li>
  </ul>
  <div class="abs photo-grid">
    <div class="photo photo--a" role="img" aria-label="Living room corner with plant"></div>
    <div class="photo photo--b" role="img" aria-label="Bedroom with purple cushion"></div>
    <div class="photo photo--c" role="img" aria-label="Modern dark kitchen counter"></div>
    <div class="photo photo--d" role="img" aria-label="Dark bedroom with lamp"></div>
    <div class="photo photo--e" role="img" aria-label="Bright room with large windows"></div>
    <div class="photo photo--f" role="img" aria-label="Bed with patterned pillows"></div>
    <div class="photo photo--g" role="img" aria-label="Bathtub with candles"></div>
    <div class="photo photo--h" role="img" aria-label="White dining area"></div>
    <div class="photo photo--i" role="img" aria-label="Room with wooden floor and plant"></div>
  </div>
  <div class="abs call-band">Call Us Today: 0055667788</div>
  <div class="abs art-mascot" role="img" aria-label="Company mascot worker in hard hat and tool belt holding up keys"></div>
  <div class="abs art-house" role="img" aria-label="Model house with red roof held on a gloved hand"></div>
</section>

<!-- Back side -->
<section class="postcard postcard--back">
  <div class="abs back-banner-top"></div>
  <div class="abs back-banner-side"></div>
  <div class="abs back-mascot" role="img" aria-label="Company mascot worker holding a model house and keys"></div>
  <p class="abs back-headline">EVERYTHING UNDER ONE ROOF<br>Interior and Exterior<br>Remodeling including<br>Room Additions and<br>New Construction.</p>

  <div class="abs stamp-box">Place<br>Stamp<br>Here</div>

  <div class="abs address-area"></div>
  <div class="abs address-line address-line--1"></div>
  <div class="abs address-line address-line--2"></div>
  <div class="abs address-line address-line--3"></div>

  <div class="abs services-panel">
    <h2 class="abs services-tab">WE ARE DOING:</h2>
    <ul class="abs service-list back-services back-services--left">
      <li><svg class="tick tick--small"><use href="#tick-ink"/></svg>Hardwood Floors</li>
      <li><svg class="tick tick--small"><use href="#tick-ink"/></svg>Ceramic Tile</li>
      <li><svg class="tick tick--small"><use href="#tick-ink"/></svg>Baseboards</li>
      <li><svg class="tick tick--small"><use href="#tick-ink"/></svg>Drywall Repairs</li>
      <li><svg class="tick tick--small"><use href="#tick-ink"/></svg>Electric etc.</li>
    </ul>
    <ul class="abs service-list back-services back-services--right">
      <li><svg class="tick tick--small"><use href="#tick-ink"/></svg>Painting</li>
      <li><svg class="tick tick--small"><use href="#tick-ink"/></svg>Casings</li>
      <li><svg class="tick tick--small"><use href="#tick-ink"/></svg>Doors</li>
      <li><svg class="tick tick--small"><use href="#tick-ink"/></svg>Plumbing</li>
    </ul>
  </div>
</section>

</body>
</html>
```